Business Card Design

Certified KFL Instructor. Self defense instruction. Ladies classes available. Semi automatic and revolver

Industry/Entity Type

Defense

```html
<!DOCTYPE html>
<html lang="en">
<head>
<meta charset="utf-8">
<title>Dana Whitfield – Business Card</title>
<link rel="stylesheet" href="https://fonts.googleapis.com/css2?family=Arimo:wght@700&family=Marcellus&display=swap">
<style>
  :root {
    --teal: #2794a6;
    --cyan: #48d9d8;
    --charcoal: #2c3432;
    --white: #ffffff;
    --dash: rgba(255, 255, 255, 0.4);
  }
  html, body {
    margin: 0;
    padding: 0;
    width: 1200px;
    height: 686px;
    overflow: hidden;
    background: var(--white);
  }
  .card {
    position: relative;
    width: 1200px;
    height: 686px;
    background: var(--white);
    border-radius: 0 0 22px 22px;
    overflow: hidden;
  }
  .card-shapes {
    position: absolute;
    inset: 0;
    width: 1200px;
    height: 686px;
  }
  .name-band {
    position: absolute;
    left: 0;
    top: 83px;
    width: 1200px;
    height: 94px;
    display: flex;
    align-items: center;
    padding-left: 43px;
    box-sizing: border-box;
  }
  .name {
    margin: 0;
    font-family: "Marcellus", serif;
    font-weight: 400;
    font-size: 60px;
    line-height: 1;
    color: var(--white);
    letter-spacing: 0.5px;
  }
  .contact {
    position: absolute;
    left: 592px;
    top: 234px;
    margin: 0;
    font-family: "Arimo", Arial, sans-serif;
    font-weight: 700;
    font-size: 34px;
    line-height: 41px;
    color: var(--teal);
    font-style: normal;
  }
  .contact span { display: block; }
  .services {
    position: absolute;
    left: 40px;
    top: 355px;
    margin: 0;
    padding: 0;
    list-style: none;
    font-family: "Arimo", Arial, sans-serif;
    font-weight: 700;
    font-size: 37px;
    line-height: 47px;
    color: var(--charcoal);
  }
  .services li {
    display: flex;
    align-items: center;
  }
  .services li::before {
    content: "";
    width: 17px;
    height: 17px;
    border: 4.5px solid var(--teal);
    border-radius: 50%;
    margin-right: 9px;
    flex: none;
  }
</style>
</head>
<body>
<div class="card">
  <svg class="card-shapes" viewBox="0 0 1050 600" preserveAspectRatio="none" aria-hidden="true">
    <rect class="name-band-fill" x="0" y="73" width="1050" height="82" fill="var(--teal)"/>
    <line x1="0" y1="80" x2="1050" y2="80" stroke="var(--dash)" stroke-width="1.5" stroke-dasharray="10 5"/>
    <line x1="0" y1="148" x2="1050" y2="148" stroke="var(--dash)" stroke-width="1.5" stroke-dasharray="10 5"/>
    <path class="corner-swoosh" d="M815,517 C955,508 1020,430 1050,335 L1050,517 Z" fill="var(--teal)"/>
    <path class="corner-swoosh-inner" d="M925,517 C990,497 1030,460 1050,412 L1050,517 Z" fill="var(--cyan)"/>
    <rect class="band-light" x="0" y="517" width="1050" height="41" fill="var(--cyan)"/>
    <rect class="band-dark" x="0" y="557" width="1050" height="43" fill="var(--charcoal)"/>
  </svg>

  <header class="name-band">
    <h1 class="name">Dana Whitfield</h1>
  </header>

  <address class="contact">
    <span class="contact-email">email - whitfieldds@mailpost.com</span>
    <span class="contact-phone">Phone 601-555-0173</span>
  </address>

  <ul class="services">
    <li>Certified KFL Instructor</li>
    <li>Self defense instruction</li>
    <li>Ladies classes available</li>
    <li>Semi automatic and revolver</li>
  </ul>
</div>
</body>
</html>
```